Willow Glow & Laser - Business Banner with Brand Elements

Design:
• We would like to get a creative design for a wide banner that will go outside our medical spa clinic location. We need a designer to make a simple yet colorful and high-quality design layout. We want this banner to be eye-catching and to communicate the services we offer at our business: Laser Hair Removal | Velonix | Lip Filler.

Requirements:
• We would like the banner to include our companies information which is the following:

Logo
“Refresh Your Skin”
Laser Hair Removal | Velonix | Lip Filler
(555) 287-1936
www.WillowGlowLaser.com

Colors:
• Our business colors are orange, a hint of black and white, but mostly peach/orange tones. (Orange: #f78f20 , White: #ffffff)

Fonts:
• Josefins Sans Bold & Lato

Content and images can be located here:
https://files.cloudvaultshare.com/folders/7tQmZ2xVbR9kLpN4sW8yH3cD6fJ1gA0eU?usp=sharing

The following will give you an idea of our brand presentation:
• Our website is: www.WillowGlowLaser.com
• Our Instagram; @willowglowlaser
• Our Facebook: www.socialpagehub.com/willowglowlaser

Target Market(s)
• Women 25 - 45

Industry/Entity Type
• Beauty

```html
<!DOCTYPE html>
<html lang="en">
<head>
<meta charset="utf-8">
<title>Willow Glow &amp; Laser – Outdoor Banner</title>
<link rel="stylesheet" href="https://fonts.googleapis.com/css2?family=Josefin+Sans:wght@700&family=Lato:wght@400;700&family=Montserrat:wght@300;700&display=swap">
<style>
  :root {
    --page-bg: #e9d3c0;
    --coral: #e06a6c;
    --orange-deep: #e8602a;
    --orange-mid: #ec7637;
    --orange-brand: #f78f20;
    --orange-light: #f5962e;
    --white: #ffffff;
    --ink: #333333;
    --photo-warm: #f0b45a;
    --photo-cool: #b9c4bf;
  }
  * { margin: 0; padding: 0; box-sizing: border-box; }
  html, body {
    width: 977px; height: 1200px; overflow: hidden;
    background: var(--page-bg);
  }
  .banner {
    position: absolute;
    left: 38px; top: 429px;
    width: 900px; height: 342px;
    overflow: hidden;
    box-shadow: 0 4px 10px rgba(0,0,0,0.25);
    color: var(--white);
  }
  .banner-art { position: absolute; inset: 0; }
  .brand {
    position: absolute;
    left: 0; width: 474px; top: 38px;
    display: flex; justify-content: center; align-items: center; gap: 10px;
  }
  .brand-dot {
    width: 30px; height: 30px; border-radius: 50%;
    background: var(--white);
  }
  .brand-name {
    font-family: "Josefin Sans", sans-serif;
    font-weight: 700; font-size: 28px; line-height: 1;
    padding-top: 5px;
  }
  .tagline-frame {
    position: absolute;
    left: 19px; top: 157px; width: 437px; height: 113px;
  }
  .headline {
    position: absolute;
    left: 0; width: 474px; top: 138px;
    text-align: center;
    font-family: "Montserrat", sans-serif;
    font-size: 35px; line-height: 40px; letter-spacing: -0.3px;
    white-space: nowrap;
  }
  .headline-strong { font-weight: 700; }
  .headline-light { font-weight: 300; }
  .services {
    position: absolute;
    left: 0; width: 474px; top: 196px;
    text-align: center;
    font-family: "Lato", sans-serif;
    font-weight: 700; font-size: 15px; letter-spacing: -0.2px;
    white-space: nowrap;
  }
  .phone-pill {
    position: absolute;
    left: 87px; top: 246px; width: 301px; height: 44px;
  }
  .phone-number {
    position: absolute;
    left: 160px; top: 246px; height: 44px;
    display: flex; align-items: center;
    font-family: Arial, "Helvetica Neue", sans-serif;
    font-weight: 700; font-size: 26px; color: var(--ink);
    white-space: nowrap;
  }
  .phone-icon { position: absolute; left: 121px; top: 256px; width: 24px; height: 24px; }
  .website {
    position: absolute;
    left: 0; width: 474px; top: 308px;
    text-align: center;
    font-family: "Lato", sans-serif;
    font-weight: 400; font-size: 14px;
  }
</style>
</head>
<body>
  <section class="banner">
    <svg class="banner-art" width="900" height="342" viewBox="0 0 900 342">
      <defs>
        <linearGradient id="bannerGradient" x1="0" y1="1" x2="1" y2="0">
          <stop offset="0" stop-color="var(--coral)"/>
          <stop offset="0.6" stop-color="var(--orange-deep)"/>
        </linearGradient>
        <linearGradient id="photoGradient" x1="0" y1="0" x2="1" y2="1">
          <stop offset="0" stop-color="#eef1ee"/>
          <stop offset="0.45" stop-color="var(--photo-cool)"/>
          <stop offset="1" stop-color="var(--photo-warm)"/>
        </linearGradient>
      </defs>
      <rect class="banner-bg" width="900" height="342" fill="url(#bannerGradient)"/>
      <path class="wave-mid" fill="var(--orange-mid)"
            d="M505,0 C470,60 505,120 545,180 C575,230 590,290 585,342 L900,342 L900,0 Z"/>
      <path class="wave-light" fill="var(--orange-light)"
            d="M538,0 C500,40 495,110 515,165 C540,225 580,285 597,342 L900,342 L900,0 Z"/>
      <path class="wave-edge" fill="#d9c6c2"
            d="M558,0 C512,40 505,110 525,165 C550,225 600,285 615,342 L900,342 L900,0 Z"/>
      <path class="hero-photo" role="img" aria-label="Photo of a smiling woman with long wavy hair and sunglasses, wearing an orange off-shoulder top, in a sunny city setting"
            fill="url(#photoGradient)"
            d="M566,0 C522,40 515,110 535,165 C560,225 610,285 630,342 L900,342 L900,0 Z"/>
    </svg>

    <div class="brand">
      <span class="brand-dot"></span>
      <span class="brand-name">Willow Glow &amp; Laser</span>
    </div>

    <svg class="tagline-frame" viewBox="0 0 437 113" fill="none" stroke="#ffffff" stroke-width="1">
      <path d="M12,0.5 H0.5 V112.5 H53"/>
      <path d="M425,0.5 H436.5 V112.5 H383"/>
    </svg>

    <h1 class="headline"><span class="headline-strong">REFRESH</span> <span class="headline-light">YOUR SKIN</span></h1>
    <p class="services">LASER HAIR REMOVAL • VELONIX • LIP FILLER</p>

    <svg class="phone-pill" viewBox="0 0 301 44">
      <polygon points="20,0 281,0 301,22 281,44 20,44 0,22" fill="#ffffff"/>
    </svg>
    <svg class="phone-icon" viewBox="0 0 24 24">
      <circle cx="12" cy="12" r="12" fill="var(--orange-brand)"/>
      <path d="M8.2,6.2 l2,2.2 -1.1,1.6 c0.8,1.8 2.2,3.2 3.9,4 l1.6,-1.1 2.2,2 -1.3,2 c-4.4,-0.5 -8.4,-4.5 -8.9,-8.9 z" fill="#ffffff"/>
    </svg>
    <p class="phone-number">(555) 287-1936</p>

    <p class="website">www.WillowGlowLaser.com</p>
  </section>
</body>
</html>
```